Rapidly growing regional logistics company looking for a modern clean website design.

We need a website for a 5 year old company based in New England.
We offer a complete logistics solution. With services dedicated to the changing economic environment. Services to our customers include, same day delivery, trucking and van service, warehouse & storage, pool distribution, and B2B installations.
We've implemented leading technology along the way, that provides visibility, accountability, up to the minute tracking, and project management.
Our goal to be known in the industry we service as an excellent provider of time-critical services and dependability.
Independently of the services we offer, our customers know that they can count on a true partner.

Target Market(s)

B2B, including printers, retail, manufacturers, wholesalers, electronics, any company that needs product delivered or warehoused

Industry/Entity Type

Logistics

Coding

Coded - Design and coding required

Number of Pages Required

5+ page

Font styles to use
Sans Serif

Colors
0255a3

Requirements
Must have
• Clean, modern design, limited clutter. Limited tabs, preferred everything on 1st screen roll down to see info

```html
<!DOCTYPE html>
<html lang="en">
<head>
<meta charset="UTF-8">
<title>Ashford Logistics – Complete Logistics Solution</title>
<link href="https://fonts.googleapis.com/css2?family=Archivo+Black&family=Open+Sans:wght@400;600&display=swap" rel="stylesheet">
<style>
  :root {
    --brand-blue: #0255a3;
    --brand-blue-dark: #024a8e;
    --nav-active: #3fb7c9;
    --nav-text: #555a60;
    --header-bg: #ffffff;
    --white: #ffffff;
    --hero-light: #f2f4f6;
    --hero-mid: #c9cfd6;
    --hero-dark: #8d969f;
    --hero-accent: #7fcf5a;
  }
  * { margin: 0; padding: 0; box-sizing: border-box; }
  html, body {
    width: 1200px;
    height: 483px;
    overflow: hidden;
    background: var(--white);
    font-family: "Open Sans", Arial, sans-serif;
  }
  .site {
    width: 1200px;
    height: 483px;
    display: flex;
    flex-direction: column;
  }
  .site-header {
    height: 70px;
    background: var(--header-bg);
    display: flex;
    align-items: center;
    justify-content: space-between;
    padding: 0 70px 0 60px;
  }
  .brand {
    display: flex;
    align-items: center;
    gap: 10px;
  }
  .brand-dot {
    width: 30px;
    height: 30px;
    border-radius: 50%;
    background: var(--brand-blue);
  }
  .brand-name {
    font-weight: 600;
    font-size: 17px;
    letter-spacing: 2px;
    color: var(--brand-blue);
  }
  .main-nav {
    display: flex;
    gap: 22px;
    list-style: none;
  }
  .main-nav a {
    text-decoration: none;
    font-size: 12px;
    letter-spacing: 0.5px;
    color: var(--nav-text);
  }
  .main-nav a.is-active { color: var(--nav-active); }
  .hero {
    position: relative;
    height: 235px;
    display: flex;
    align-items: center;
    justify-content: center;
    overflow: hidden;
  }
  .hero-visual {
    position: absolute;
    inset: 0;
    background:
      radial-gradient(ellipse 180px 60px at 55% 62%, rgba(127,207,90,0.55), transparent 70%),
      linear-gradient(160deg, var(--hero-light) 0%, var(--hero-mid) 45%, var(--hero-light) 70%, var(--hero-dark) 100%);
  }
  .hero-title {
    position: relative;
    font-family: "Archivo Black", "Arial Black", sans-serif;
    font-size: 52px;
    letter-spacing: 0.5px;
    color: var(--brand-blue);
    text-transform: uppercase;
  }
  .intro {
    flex: 1;
    background: var(--brand-blue);
    display: grid;
    grid-template-columns: 1fr 1fr;
    gap: 60px;
    padding: 28px 80px 0 60px;
    color: var(--white);
  }
  .intro p {
    font-size: 12px;
    line-height: 1.45;
    margin-bottom: 14px;
    max-width: 430px;
  }
</style>
</head>
<body>
  <div class="site">
    <header class="site-header">
      <div class="brand">
        <span class="brand-dot"></span>
        <span class="brand-name">ASHFORD</span>
      </div>
      <nav>
        <ul class="main-nav">
          <li><a href="#about" class="is-active">ABOUT</a></li>
          <li><a href="#info">INFO</a></li>
          <li><a href="#contact">CONTACT</a></li>
        </ul>
      </nav>
    </header>

    <section class="hero">
      <div class="hero-visual" role="img" aria-label="Aerial view of rows of white delivery trucks on a highway with one truck highlighted in green"></div>
      <h1 class="hero-title">Complete Logistics Solution</h1>
    </section>

    <section class="intro" id="about">
      <div class="intro-col">
        <p>Our company was founded in 2012 but our team is seasoned with a combined 75 years of experience.</p>
        <p>Ashford Logistics offers a complete logistics solution. With services dedicated to the changing economic environment.</p>
        <p>Services to our customers include, same day delivery, trucking and van service, warehouse &amp; storage, pool distribution, and B2B white glove installations.</p>
      </div>
      <div class="intro-col">
        <p>We've implemented leading technology along the way, that provides visibility, accountability, up to the minute tracking, and project management.</p>
        <p>Our goal to be known in the industry we service as an excellent provider of time-critical services and dependability.</p>
        <p>Independently of the services we offer, our customers know that they can count on a true partner.</p>
      </div>
    </section>
  </div>
</body>
</html>
```